Quiet Harbor Hours Podcast Artwork

I need a cover for my podcast Quiet Harbor Hours that is clean, modern, and minimalist, but not too feminine

Target Market(s)

People struggling with fertility particularly women who are between the ages of 35-45 though there is a small set of listeners who are men

Requirements
Must have
• Embryo in the Zero
Should not have
• No script text

```html
<!DOCTYPE html>
<html lang="en">
<head>
<meta charset="UTF-8">
<title>Quiet Harbor Hours – Podcast Cover</title>
<link rel="stylesheet" href="https://fonts.googleapis.com/css2?family=Josefin+Sans:wght@600&display=swap">
<style>
  :root {
    --page-bg: #efefef;
    --cover-brown: #7a4a36;
    --cover-brown-light: #84563f;
    --cover-brown-deep: #5e3524;
    --cream: #f8e3d9;
    --sage: #9fad8a;
  }
  * { box-sizing: border-box; margin: 0; padding: 0; }
  html, body {
    width: 1200px;
    height: 800px;
    overflow: hidden;
  }
  body {
    background: var(--page-bg);
    display: flex;
    align-items: center;
    justify-content: center;
    font-family: "Josefin Sans", sans-serif;
  }
  .podcast-cover {
    position: relative;
    width: 600px;
    height: 600px;
    background: var(--cover-brown);
    overflow: hidden;
  }
  .cover-backdrop {
    position: absolute;
    inset: 0;
    background: radial-gradient(circle at 58% 42%,
      var(--cover-brown-deep) 0%,
      var(--cover-brown) 45%,
      var(--cover-brown-light) 100%);
  }
  .wordmark {
    position: absolute;
    inset: 0;
    display: flex;
    flex-direction: column;
    align-items: center;
    justify-content: center;
    gap: 34px;
  }
  .wordmark-dot {
    width: 64px;
    height: 64px;
    border-radius: 50%;
    background: var(--sage);
  }
  .show-title {
    color: var(--cream);
    font-weight: 600;
    font-size: 78px;
    line-height: 0.98;
    letter-spacing: 1px;
    text-transform: uppercase;
    text-align: center;
  }
</style>
</head>
<body>
  <main class="podcast-cover">
    <div class="cover-backdrop" role="img" aria-label="Radiating sunburst pattern in warm brown tones"></div>
    <div class="wordmark">
      <span class="wordmark-dot"></span>
      <h1 class="show-title">Quiet<br>Harbor<br>Hours</h1>
    </div>
  </main>
</body>
</html>
```